Business Card Design needed for logo design project

Our company needs a Business Card Design. Please refer to our original project in the link above.
Dorian Pellworth
Broker

W: Velvetcrestestates.example
P: 555-302-7184
F: 555-741-2096
E: dorianpellworth@mailbox.example
A: North Dallas Office
Updates

Name Spelling update , sorry Dorian Pellworth card is double sided

```html
<!DOCTYPE html>
<html lang="en">
<head>
<meta charset="utf-8">
<title>Dorian Pellworth – Business Card</title>
<link rel="stylesheet" href="https://fonts.googleapis.com/css2?family=Libre+Baskerville:wght@400;700&family=Open+Sans:wght@400&display=swap">
<style>
  :root {
    --page-bg: #f4f4f4;
    --navy: #1f2c5c;
    --card-white: #f7f7f7;
    --ink: #111111;
    --gold: #b48a4a;
    --green: #2f9a6b;
    --card-shadow: rgba(0, 0, 0, 0.18);
  }
  * { box-sizing: border-box; margin: 0; padding: 0; }
  html, body {
    width: 1200px;
    height: 418px;
    overflow: hidden;
    background: var(--page-bg);
  }
  .canvas {
    position: relative;
    width: 1200px;
    height: 418px;
  }
  .card {
    position: absolute;
    top: 38px;
    width: 516px;
    height: 328px;
    box-shadow: 0 3px 10px var(--card-shadow);
    overflow: hidden;
  }
  .card--front { left: 72px; background: var(--card-white); }
  .card--back { left: 638px; background: var(--navy); }

  .brand-panel {
    position: absolute;
    left: 0; top: 0;
    width: 234px;
    height: 100%;
    background: var(--navy);
  }
  .brand {
    position: absolute;
    left: 0; right: 0;
    display: flex;
    flex-direction: column;
    align-items: center;
    text-align: center;
  }
  .brand__mark {
    border-radius: 50%;
    background: var(--gold);
  }
  .brand__name {
    font-family: "Libre Baskerville", Georgia, serif;
    font-weight: 400;
    color: var(--gold);
    text-transform: uppercase;
    letter-spacing: 0.04em;
    line-height: 1.25;
  }
  .brand--front { top: 70px; }
  .brand--front .brand__mark { width: 90px; height: 90px; margin-bottom: 28px; }
  .brand--front .brand__name { font-size: 17px; }

  .brand--back { top: 66px; }
  .brand--back .brand__mark { width: 96px; height: 96px; margin-bottom: 30px; }
  .brand--back .brand__name { font-size: 20px; }

  .identity {
    position: absolute;
    left: 278px;
    top: 40px;
    width: 214px;
  }
  .identity__name {
    font-family: "Libre Baskerville", Georgia, serif;
    font-weight: 700;
    font-size: 21px;
    color: var(--ink);
    white-space: nowrap;
  }
  .identity__role {
    font-family: "Open Sans", Arial, sans-serif;
    font-size: 15px;
    color: var(--gold);
    text-align: right;
    margin-top: 2px;
  }
  .identity__rule {
    height: 2px;
    background: var(--green);
    margin-top: 6px;
  }

  .contact {
    position: absolute;
    left: 246px;
    right: 16px;
    top: 200px;
    font-family: "Open Sans", Arial, sans-serif;
    font-size: 14px;
    line-height: 21px;
    color: var(--ink);
    text-align: right;
    white-space: nowrap;
    list-style: none;
  }
</style>
</head>
<body>
<main class="canvas">
  <section class="card card--front" aria-label="Business card front">
    <div class="brand-panel" role="img" aria-label="Navy panel with fine dotted texture">
      <div class="brand brand--front">
        <span class="brand__mark"></span>
        <span class="brand__name">Velvetcrest<br>Estates</span>
      </div>
    </div>
    <div class="identity">
      <h1 class="identity__name">Dorian Pellworth</h1>
      <p class="identity__role">broker</p>
      <div class="identity__rule"></div>
    </div>
    <ul class="contact">
      <li>P: 555-302-7184</li>
      <li>F: 555-741-2096</li>
      <li>E: dorianpellworth@mailbox.example</li>
      <li>W: Velvetcrestestates.example</li>
    </ul>
  </section>

  <section class="card card--back" role="img" aria-label="Business card back, navy with fine dotted texture">
    <div class="brand brand--back">
      <span class="brand__mark"></span>
      <span class="brand__name">Velvetcrest<br>Estates</span>
    </div>
  </section>
</main>
</body>
</html>
```